Wine Label - Design required by La Brisuela

2 Independent chilean winemakers here!
La Brisuela (means door slam or slam), that is the brand for our wines (2 wines at the moment), low scale production.
We would like to have front label for our wine out of the mainstream typical french classic style. Some words to describe it: youthful yet vintage/ Tobiah Vance/ pellman/ comic/ old western. Something i would wear on a t-shirt.
The text that is has to be on the label:
- La Brisuela (the brand)
-Field Blend (the type of one of the wines we have)
- 2018
- Wine of Chile.
It goes on sloping shoulder bottle, Burgundy model.
It is meant to cover a space of 3 1/4 h x 4 1/2 w inches . (or 8,5 cm height x 11cm width).
We like colours so...be creative!
I have attached the "La Brisuela" logo. We can changed it of course.
Thanks !

Target Market(s)

young drinkers (legally allowed to drink!)

Font styles to use
Other font styles liked:
• stencil

Colors

Designer to choose colors to be used in the design.

Requirements
Should not have
• Obvious wine things like glasses of wine, vines, grapes etc.

```html
<!DOCTYPE html>
<html lang="en">
<head>
<meta charset="utf-8">
<title>La Brisuela – Field Blend Label</title>
<link rel="stylesheet" href="https://fonts.googleapis.com/css2?family=Stardos+Stencil:wght@400;700&display=swap">
<style>
  :root {
    --label-yellow: #f2ea1e;
    --ink-navy: #3a3486;
  }
  html, body {
    margin: 0;
    padding: 0;
    width: 1200px;
    height: 927px;
    overflow: hidden;
    background: var(--label-yellow);
  }
  .label {
    position: relative;
    width: 1200px;
    height: 927px;
    background: var(--label-yellow);
    color: var(--ink-navy);
    font-family: "Stardos Stencil", "Times New Roman", serif;
    font-weight: 700;
  }
  .label-frame {
    position: absolute;
    inset: 0;
  }
  .corner-ornament {
    fill: var(--ink-navy);
    opacity: 0.85;
  }
  .line {
    position: absolute;
    left: 0;
    width: 1200px;
    margin: 0;
    text-align: center;
    line-height: 1;
    white-space: nowrap;
  }
  .origin {
    top: 126px;
    font-size: 66px;
    letter-spacing: 0.04em;
  }
  .vintage {
    top: 236px;
    font-size: 72px;
    letter-spacing: 0.35em;
    padding-left: 0.35em;
    box-sizing: border-box;
  }
  .brand-name {
    top: 460px;
    font-size: 118px;
    letter-spacing: 0.02em;
  }
  .wine-type {
    top: 672px;
    font-size: 72px;
    letter-spacing: 0.03em;
  }
  .spec {
    position: absolute;
    top: 690px;
    width: 120px;
    margin: 0;
    text-align: center;
    font-size: 27px;
    line-height: 56px;
  }
  .spec-volume { left: 90px; }
  .spec-alcohol { left: 990px; }
  .spec span { display: block; }
</style>
</head>
<body>
  <main class="label">
    <svg class="label-frame" width="1200" height="927" viewBox="0 0 1200 927">
      <g stroke="var(--ink-navy)" stroke-width="9" stroke-linecap="round" fill="none">
        <line x1="300" y1="60" x2="900" y2="60"/>
        <line x1="300" y1="867" x2="900" y2="867"/>
        <line x1="36" y1="190" x2="36" y2="717"/>
        <line x1="1164" y1="190" x2="1164" y2="717"/>
      </g>
      <rect class="corner-ornament" x="24" y="24" width="240" height="140" rx="18" role="img" aria-label="Curled scroll corner ornament, top left"/>
      <rect class="corner-ornament" x="936" y="24" width="240" height="140" rx="18" role="img" aria-label="Curled scroll corner ornament, top right"/>
      <rect class="corner-ornament" x="24" y="815" width="240" height="88" rx="18" role="img" aria-label="Curled scroll corner ornament, bottom left"/>
      <rect class="corner-ornament" x="936" y="815" width="240" height="88" rx="18" role="img" aria-label="Curled scroll corner ornament, bottom right"/>
    </svg>

    <p class="line origin">WINE OF CHILE</p>
    <p class="line vintage">2018</p>
    <h1 class="line brand-name">LA BRISUELA</h1>
    <p class="line wine-type">FIELD BLEND</p>

    <p class="spec spec-volume"><span>750</span><span>ML</span></p>
    <p class="spec spec-alcohol"><span>15%</span><span>VOL</span></p>
  </main>
</body>
</html>
```